Commercial Rooftop Solar business needs a website

We need a website with fantastic appeal for a new company based in Melbourne called Tidewell Energy. We design and install solar energy systems for commercial applications across Australia. Our market is to focus on small to medium businesses looking for solar solutions, but we will also provide our service for residential customers. We would like a beautiful 'front page' feel to our home page, using photographs of solar PV systems and/or natural imagery. Our logo uses the colours orange and black, which could easily be echoed in photographic imagery of sunset and sunrise, for example. The design should communicate quiet confidence and professionalism to a corporate marketplace.

NEW POINTS FOR BRIEF: This design also needs to be flexible to allow for additional future content, including a Support page with sub pages, FAQ's, and a Blog.

As part of this design project, we will require the coding for the website to be completed by the designer.

We have seen some websites, which we like the look and feel of: these are listed below.

brightquarrypower.com.au:

• Beautiful images underlaying brief text selling points.
• Simple ‘front cover’ style home page with elegant drop-down menu, stylish simple font style.
• Home page invites exploration through the menu links, rather than trying to provide all the information up front.
• Company logo and name in the top left hand corner, contact details accessible at top right hand, seems consistent in most sites.

fonvaleenergy.com.au

murlockenergy.com:
• Same element as the others is the front-page style home page with beautiful images underlying text.

We have a webpage that we started uploading content to. You can use some of the content there in your designs: www.tidewellenergy.com.au

Technical Specifications:
PAGES:

Home

About Us

Solutions - Commercial
- Residential

Products - Solar Panels - Vorla Kestrel, Vorla TUSK, Vorla QB
- Solar Inverters - Delmark, VoltHaven
- Monitoring systems - Grid Insight
- Batteries - KD

- Datasheets have been provided for reference but if it's too much work, you can use generic text and we will provide content later.

Contact Us

FUTURE PAGES (Please consider in structure, where links could be placed):

Support

FAQ's

Blog.

We could provide some content for the Support page soon, but the Blog and FAQ's are future pages which we don't want highlighted in the design as we don't yet have content.

Phone: 1800 7 TIDEW
Email: sales@tidewellenergy.com.au

Currently, I do not have images and text available. Please
use placeholders in the meantime. The final text and images will be uploaded for the winner once a winning design has been selected.

Target Market(s)

Primary focus is on small to medium sized business owners. Those owners will have a house which may be suitable for solar so we want to cater to residential deeper in the website.

Industry/Entity Type

Solar Energy

Coding

Coded - Design and coding required

Number of Pages Required

5+ page

Colors
f78f20
0255a3

Requirements
Must have
• Logo as per attachments.
Nice to have
• Logo can have alternate colours Eg. White on Orange or Black etc. provided colour correct logo is shown somewhere eg. footer or contact page.
• In the active site, I'd like to have:
• Very slowly zooming images - barely perceptible.
• Title text that rolls into place
• Subtle movements
• See https://pellbrook.com.au/ for example

```html
<!DOCTYPE html>
<html lang="en">
<head>
<meta charset="utf-8">
<title>Tidewell Energy</title>
<link rel="stylesheet" href="https://fonts.googleapis.com/css2?family=Open+Sans:wght@400;600;700&family=Mulish:wght@400;500;600&display=swap">
<style>
:root{
  --orange:#ef5a24;
  --ink:#1f1f1f;
  --text:#4a4a4a;
  --muted:#9a9a9a;
  --line:#e1e1e1;
  --white:#ffffff;
  --social:#ef5a24;
}
*{box-sizing:border-box;margin:0;padding:0}
html,body{width:672px;height:1200px;overflow:hidden;background:var(--white)}
body{position:relative;font-family:"Mulish",sans-serif;color:var(--text)}
.abs{position:absolute}

/* header */
.site-header{position:absolute;left:0;top:0;width:672px;height:58px}
.brand{position:absolute;left:75px;top:16px;display:flex;align-items:center;gap:8px}
.brand-dot{width:24px;height:24px;border-radius:50%;background:var(--ink)}
.brand-name{font-family:"Open Sans",sans-serif;font-weight:600;font-size:17px;color:var(--orange);letter-spacing:.5px}
.topbar{position:absolute;right:74px;top:11px;display:flex;align-items:center;font-size:7px;color:var(--muted)}
.topbar .phone{color:var(--orange);font-size:11px;margin-left:3px;margin-right:26px}
.social{display:flex;gap:3px;margin-left:6px}
.social span{width:12px;height:12px;border-radius:50%;background:var(--social)}
.main-nav{position:absolute;right:74px;top:34px;display:flex;gap:0;font-family:"Open Sans",sans-serif;font-weight:600;font-size:7px;color:var(--ink)}
.main-nav a{display:block;text-decoration:none;color:inherit;padding:5px 0;margin-left:38px}
.main-nav a.active{background:var(--orange);color:var(--white);padding:5px 5px;margin-left:0}

/* hero */
.hero{position:absolute;left:0;top:58px;width:672px;height:316px;
  background:linear-gradient(110deg,#3a2a35 0%,#b4582c 12%,#443a5a 28%,#2c3560 50%,#1d2547 75%,#14182e 100%)}
.hero-title{position:absolute;left:209px;top:151px;width:254px;height:58px;border:1.5px solid rgba(255,255,255,.85);
  display:flex;align-items:center;justify-content:center;text-align:center;
  font-family:"Open Sans",sans-serif;font-weight:700;font-size:24px;line-height:26px;color:var(--white)}
.slider-dots{position:absolute;left:307px;top:330px;display:flex;gap:7px;align-items:center}
.slider-dots span{width:5px;height:5px;border-radius:50%;background:var(--white)}
.slider-dots span.current{width:7px;height:7px;background:transparent;border:1.2px solid var(--white)}

/* solutions */
.section-title{position:absolute;left:0;width:672px;text-align:center;font-family:"Open Sans",sans-serif;font-weight:700;font-size:16px;color:var(--orange)}
.section-intro{position:absolute;left:196px;top:446px;width:280px;text-align:center;font-size:7.5px;line-height:12.5px;color:var(--text)}
.solution-card{position:absolute;top:518px;width:252px;height:177px;border:1px solid var(--line);text-align:center}
.solution-icon{position:absolute;left:100px;top:-17px;width:52px;height:52px;border-radius:50%;background:var(--orange);display:flex;align-items:center;justify-content:center}
.solution-card h3{position:absolute;left:0;top:51px;width:100%;font-family:"Mulish",sans-serif;font-weight:600;font-size:10px;color:var(--ink)}
.solution-card p{position:absolute;left:22px;top:75px;width:208px;font-size:6.6px;line-height:11.2px;color:var(--text)}
.btn-outline{position:absolute;display:flex;align-items:center;justify-content:center;border:1px solid var(--orange);color:var(--orange);font-size:6.8px;font-weight:500}
.solution-card .btn-outline{left:96px;top:139px;width:60px;height:19px}

/* welcome */
.welcome{position:absolute;left:0;top:730px;width:672px;height:250px;
  background:radial-gradient(ellipse at 80% 60%,#c8691c 0%,rgba(120,60,20,.6) 25%,transparent 50%),
  linear-gradient(180deg,#3e2a1e 0%,#5b3519 35%,#6a3c17 55%,#2a1a10 80%,#1a120c 100%)}
.welcome h2{position:absolute;left:0;top:41px;width:672px;text-align:center;font-family:"Open Sans",sans-serif;font-weight:700;font-size:15px;color:var(--white)}
.welcome p{position:absolute;left:176px;top:78px;width:320px;text-align:center;font-size:8.2px;line-height:14px;color:var(--white)}
.welcome .btn-outline{left:305px;top:170px;width:62px;height:22px;color:var(--orange)}

/* footer */
.site-footer{position:absolute;left:0;top:980px;width:672px;height:220px}
.site-footer .brand{left:75px;top:36px}
.follow{position:absolute;left:102px;top:96px;display:flex;align-items:center;font-size:7px;font-weight:600;color:var(--orange)}
.follow .social{gap:5px;margin-left:10px}
.follow .social span{width:17px;height:17px}
.footer-divider{position:absolute;left:279px;top:41px;width:1px;height:88px;background:var(--line)}
.footer-col h4{font-size:7px;font-weight:600;color:var(--orange);margin-bottom:12px}
.menu-col{position:absolute;left:334px;top:42px}
.menu-col ul{list-style:none;font-size:6.6px;line-height:11.2px;color:var(--text)}
.contact-col{position:absolute;left:461px;top:42px}
.contact-item{display:flex;font-size:6.6px;line-height:11.2px;color:var(--text);margin-bottom:14px}
.contact-item svg{width:8px;height:8px;margin-right:10px;margin-top:2px;flex:none}
.footer-rule{position:absolute;left:74px;top:160px;width:523px;height:1px;background:var(--line)}
.copyright{position:absolute;left:0;top:181px;width:672px;text-align:center;font-size:6px;color:var(--ink)}
</style>
</head>
<body>

<header class="site-header">
  <div class="brand"><span class="brand-dot"></span><span class="brand-name">TIDEWELL ENERGY</span></div>
  <div class="topbar">
    CALL US : <span class="phone">888.888.8888</span>
    FOLLOW US :
    <div class="social"><span></span><span></span><span></span></div>
  </div>
  <nav class="main-nav">
    <a class="active" href="#">HOME</a>
    <a href="#">ABOUT US</a>
    <a href="#">SOLUTIONS</a>
    <a href="#">CONTACT US</a>
  </nav>
</header>

<section class="hero" role="img" aria-label="Rooftop solar panels at sunset">
  <div class="hero-title">SOLAR ENERGY<br>SYSTEMS</div>
  <div class="slider-dots"><span></span><span class="current"></span><span></span><span></span><span></span></div>
</section>

<section class="solutions">
  <h2 class="section-title" style="top:411px">OUR SOLUTIONS</h2>
  <p class="section-intro">It is a long established fact that a reader will be distracted by the readable content of a page when looking at its layout</p>

  <article class="solution-card" style="left:75px">
    <div class="solution-icon">
      <svg width="24" height="24" viewBox="0 0 24 24" fill="none" stroke="#fff" stroke-width="1.3">
        <rect x="4" y="3" width="9" height="18"/><rect x="13" y="9" width="7" height="12"/>
        <path d="M6.5 6h1.5M9.5 6h1.5M6.5 9h1.5M9.5 9h1.5M6.5 12h1.5M9.5 12h1.5M6.5 15h1.5M9.5 15h1.5M15.5 12h2M15.5 15h2M7.5 21v-3h2v3M2 21h20"/>
      </svg>
    </div>
    <h3>Commercial</h3>
    <p>There are many variations of passages of Lorem Ipsum available, but the majority have suffered alteration in some form, by injected humour, or randomised words which don't look even There are many variations of passages of Lorem Ipsum.</p>
    <a class="btn-outline">READ MORE</a>
  </article>

  <article class="solution-card" style="left:346px">
    <div class="solution-icon">
      <svg width="26" height="26" viewBox="0 0 24 24" fill="none" stroke="#fff" stroke-width="1.5" stroke-linejoin="round">
        <path d="M2.5 12L12 3.5l9.5 8.5"/><path d="M5.5 10v10.5h13V10"/><rect x="9.5" y="14" width="5" height="6.5"/>
      </svg>
    </div>
    <h3>Residential</h3>
    <p>There are many variations of passages of Lorem Ipsum available, but the majority have suffered alteration in some form, by injected humour, or randomised words which don't look even There are many variations of passages of Lorem Ipsum.</p>
    <a class="btn-outline">READ MORE</a>
  </article>
</section>

<section class="welcome" role="img" aria-label="Sunset over a lake and forested hills">
  <h2>WELCOME TO OUR SITE</h2>
  <p>There are many variations of passages of Lorem Ipsum available, but the majority have suffered alteration in some form, by injected humour, or randomised words which don't look even slightly believable. If you are going to use a passage of Lorem Ipsum, you need to be sure there isn't anything embarrassing hidden in the middle of text. All the Lorem Ipsum</p>
  <a class="btn-outline">READ MORE</a>
</section>

<footer class="site-footer">
  <div class="brand"><span class="brand-dot"></span><span class="brand-name">TIDEWELL ENERGY</span></div>
  <div class="follow">FOLLOW US <div class="social"><span></span><span></span><span></span></div></div>
  <div class="footer-divider"></div>

  <div class="footer-col menu-col">
    <h4>MENU</h4>
    <ul><li>Home</li><li>About us</li><li>Solutions</li><li>Commercial</li><li>Residential</li><li>Contact Us</li></ul>
  </div>

  <div class="footer-col contact-col">
    <h4>CONTACT US</h4>
    <div class="contact-item">
      <svg viewBox="0 0 10 10"><path d="M5 .5a3 3 0 0 1 3 3c0 2.2-3 6-3 6s-3-3.8-3-6a3 3 0 0 1 3-3z" fill="#333"/><circle cx="5" cy="3.5" r="1" fill="#fff"/></svg>
      <span>418 Harbour Lane<br>Carlton, VIC 3053</span>
    </div>
    <div class="contact-item">
      <svg viewBox="0 0 10 10"><path d="M2.2 1l1.6 1.8-.9 1.3c.6 1.2 1.6 2.2 2.8 2.8l1.3-.9L8.8 7.6 7.8 9C4.2 8.6 1.4 5.8 1 2.2z" fill="#333"/></svg>
      <span>888.888.8888</span>
    </div>
    <div class="contact-item" style="margin-top:10px">
      <svg viewBox="0 0 10 10"><rect x="1" y="2.2" width="8" height="5.6" fill="#333"/><path d="M1 2.5l4 3 4-3" stroke="#fff" stroke-width=".8" fill="none"/></svg>
      <span>info@tidewellenergy.com</span>
    </div>
  </div>

  <div class="footer-rule"></div>
  <p class="copyright">Copyrights @ 2017 All Rights Reserved</p>
</footer>

</body>
</html>
```